creative design for a downloadable PDF

I have a PDF document that needs some creative inspiration on two pages. This PDF will be available for download from our website and contains information on a new service offering. The general design elements are finished and will not be altered: the cover page, headers/footers, color scheme, and back page are all fixed. We just have a 'Table of Contents' page and a 'Workflow' page that are uninteresting and lack inspiration. The Workflow page in particular is concerning as it fails to convey our step-by-step approach to project management and how our customers progress through the steps over time. We had a simple bulleted list (see the MS Word Doc), then went to 'tiles' which zigzag across the page (see the PDF). Anyway we need someone to display this in a more thoughtful and easily understood way.

```html
<!DOCTYPE html>
<html lang="en">
<head>
<meta charset="utf-8">
<title>The Guided Purchasing Experience – Brochure Pages</title>
<link href="https://fonts.googleapis.com/css2?family=Open+Sans:wght@400;600;700;800&family=Montserrat:wght@700;800&display=swap" rel="stylesheet">
<style>
  :root{
    --board:#9b9b9b;
    --blue:#1f74ad;
    --blue-deep:#175d8e;
    --blue-soft:#4e9bcf;
    --blue-pale:#d8e8f3;
    --ink:#3b4450;
    --muted:#7a8591;
    --white:#ffffff;
  }
  *{box-sizing:border-box;margin:0;padding:0}
  html,body{width:1200px;height:2660px;overflow:hidden}
  body{background:var(--board);font-family:"Open Sans",Arial,sans-serif;color:var(--ink);position:relative}
  .page{position:absolute;width:450px;height:632px;background:var(--white);overflow:hidden;box-shadow:0 3px 10px rgba(0,0,0,.25)}
  .page--blue{background:var(--blue)}
  .running-head,.running-foot{position:absolute;left:0;right:0;height:14px;background:var(--blue);color:var(--white);font-size:5.5px;display:flex;align-items:center;justify-content:space-between;padding:0 16px;letter-spacing:.2px}
  .running-head{top:0}
  .running-foot{bottom:0}
  .page--blue .running-head,.page--blue .running-foot{background:var(--blue-deep)}
  .section-title{font-family:"Montserrat","Open Sans",sans-serif;font-weight:700;color:var(--blue);font-size:15px}
  .body-copy{font-size:6.6px;line-height:1.55;color:var(--ink)}
  .photo{position:absolute}

  /* cover */
  .cover{left:600px;top:88px}
  .brand{position:absolute;left:22px;top:20px;display:flex;align-items:center;gap:6px;font-weight:700;font-size:17px;color:var(--blue)}
  .brand__dot{width:14px;height:14px;border-radius:50%;background:var(--blue)}
  .cover__photo{left:0;top:64px;width:450px;height:568px;background:linear-gradient(160deg,#7fb4da 0%,#2f7fb8 40%,#1a5d92 100%)}
  .cover__title{position:absolute;left:0;right:0;top:150px;text-align:center;color:var(--white)}
  .cover__title .kicker{font-family:"Montserrat",sans-serif;font-weight:800;font-size:34px;letter-spacing:1px;line-height:1}
  .cover__title .big{font-family:"Montserrat",sans-serif;font-weight:800;font-size:58px;letter-spacing:3px;line-height:1.05}
  .cover__title .sub{font-family:"Montserrat",sans-serif;font-size:26px;font-weight:800;line-height:1.1}

  /* spread 1 */
  .purchasing{left:152px;top:772px}
  .purchasing .section-title{position:absolute;left:24px;top:32px}
  .purchasing .body-copy{position:absolute;left:24px;top:56px;width:402px}
  .purchasing__photo{left:24px;top:168px;width:402px;height:290px;background:linear-gradient(135deg,#e8ecef,#b8c4cc 55%,#8c99a3)}
  .toc{left:602px;top:772px}
  .toc__head{position:absolute;left:232px;top:96px;color:var(--white)}
  .toc__head small{display:block;font-size:10px;opacity:.85}
  .toc__head strong{display:block;font-family:"Montserrat",sans-serif;font-size:20px;font-weight:700;line-height:1.15}
  .toc__rule{position:absolute;left:232px;top:160px;width:190px;height:1px;background:rgba(255,255,255,.6)}
  .toc__list{position:absolute;left:232px;top:180px;list-style:none;color:var(--white)}
  .toc__list li{margin-bottom:16px}
  .toc__list b{display:block;font-family:"Montserrat",sans-serif;font-size:22px;line-height:1}
  .toc__list span{font-size:9px}
  .toc__glow{position:absolute;left:-120px;top:200px;width:420px;height:420px;border-radius:50%;background:radial-gradient(circle,rgba(255,255,255,.12),rgba(255,255,255,0) 70%)}

  /* spread 2 */
  .escrow{left:152px;top:1448px}
  .escrow .section-title{position:absolute;left:24px;top:34px}
  .escrow .body-copy{position:absolute;left:24px;top:58px;width:402px}
  .escrow__photo{left:24px;top:272px;width:402px;height:300px;background:linear-gradient(135deg,#f2f4f6,#c9d3da 50%,#8e9ea9)}
  .workflow{left:602px;top:1448px}
  .workflow .section-title{position:absolute;left:0;right:0;top:28px;text-align:center}
  .timeline{position:absolute;left:0;top:60px}

  /* back */
  .back{left:152px;top:2140px;height:440px}
  .back__title{position:absolute;left:24px;top:28px;color:var(--white);font-family:"Montserrat",sans-serif;font-size:17px;font-weight:700}
  .back__kicker{position:absolute;left:24px;top:52px;color:var(--white);font-size:7px;opacity:.85}
  .back .body-copy{position:absolute;left:24px;top:104px;width:400px;color:var(--white)}
  .back__sign{position:absolute;left:24px;top:230px;color:var(--white);font-family:Georgia,serif;font-size:18px}
  .back__role{position:absolute;left:24px;top:256px;color:var(--white);font-size:6.5px}
  .back__contact{position:absolute;right:24px;top:320px;width:120px;text-align:left;color:var(--white);font-size:6.5px;line-height:1.6}
  .back__button{position:absolute;right:24px;top:290px;width:120px;height:16px;border-radius:8px;background:var(--white);color:var(--blue);font-size:6.5px;font-weight:700;display:flex;align-items:center;justify-content:center}
  .back__icon{position:absolute;right:24px;top:384px;width:16px;height:16px;border-radius:50%;background:var(--white)}
</style>
</head>
<body>

<section class="page cover">
  <div class="brand"><span class="brand__dot"></span>Harbor Medical</div>
  <div class="photo cover__photo" role="img" aria-label="Close-up of a hand using a tablet with digital interface, tinted blue"></div>
  <div class="cover__title">
    <div class="kicker">THE</div>
    <div class="big">GUIDED</div>
    <div class="sub">PURCHASING<br>EXPERIENCE</div>
  </div>
</section>

<section class="page purchasing">
  <div class="running-head"><span>The Guided Purchasing Experience</span><span>Harbor Medical</span></div>
  <h2 class="section-title">The Purchasing Experience</h2>
  <p class="body-copy">The Purchasing Experience from Harbor Medical was created to make buying a custom device simple, clear and predictable from the very first call. Every project follows one proven path, so you always know where things stand, what happens next and who is responsible for each step. Our team guides you through planning, pricing, design, build and delivery, sharing updates at every milestone. We keep documents, approvals and timelines in one place, which removes guesswork and reduces delays. The result is a steady process that protects your budget, respects your schedule and gives you confidence that the finished product will meet every requirement you set.</p>
  <div class="photo purchasing__photo" role="img" aria-label="Team of colleagues meeting around a table in a bright office"></div>
  <div class="running-foot"><span>www.harbormedical.example</span><span>555-010-4400</span></div>
</section>

<section class="page page--blue toc">
  <div class="running-head"><span>The Guided Purchasing Experience</span><span>Harbor Medical</span></div>
  <div class="toc__glow"></div>
  <div class="toc__head"><small>Document Set</small><strong>Table of Contents</strong></div>
  <div class="toc__rule"></div>
  <ol class="toc__list">
    <li><b>02</b><span>The Purchasing Experience</span></li>
    <li><b>03</b><span>Table of Contents</span></li>
    <li><b>04</b><span>IP Escrow</span></li>
    <li><b>05</b><span>The Guided Workflow</span></li>
  </ol>
  <div class="running-foot"><span>www.harbormedical.example</span><span>555-010-4400</span></div>
</section>

<section class="page escrow">
  <div class="running-head"><span>The Guided Purchasing Experience</span><span>Harbor Medical</span></div>
  <h2 class="section-title">IP Escrow</h2>
  <p class="body-copy">Intellectual property escrow protects both you and our team by holding the design files, source code and build records with a neutral third party. Once the project reaches the agreed stage, the complete package is deposited and verified, so you always have access to the work you paid for. If support ever ends or conditions change, the escrow agent releases the materials to you under clear terms. This gives your organization lasting security, keeps ownership transparent and lets you plan long term without depending on a single supplier for the future of your product.</p>
  <div class="photo escrow__photo" role="img" aria-label="Hands reviewing charts and documents on a desk with a laptop"></div>
  <div class="running-foot"><span>www.harbormedical.example</span><span>555-010-4400</span></div>
</section>

<section class="page workflow">
  <div class="running-head"><span>The Guided Purchasing Experience</span><span>Harbor Medical</span></div>
  <h2 class="section-title">The Guided Workflow</h2>
  <svg class="timeline" width="450" height="550" viewBox="0 0 450 550" font-family="Open Sans, Arial, sans-serif" font-size="6.6" fill="#3b4450">
    <line x1="225" y1="10" x2="225" y2="536" stroke="#1f74ad" stroke-width="2"/>
    <g fill="#1f74ad">
      <circle cx="225" cy="18" r="6"/><circle cx="225" cy="56" r="6"/><circle cx="225" cy="94" r="6"/>
      <circle cx="225" cy="132" r="6"/><circle cx="225" cy="170" r="6"/><circle cx="225" cy="208" r="6"/>
      <circle cx="225" cy="246" r="6"/><circle cx="225" cy="284" r="6"/><circle cx="225" cy="322" r="6"/>
      <circle cx="225" cy="360" r="6"/><circle cx="225" cy="398" r="6"/><circle cx="225" cy="436" r="6"/>
      <circle cx="225" cy="474" r="6"/><circle cx="225" cy="512" r="6"/>
    </g>
    <g stroke="#4e9bcf" stroke-width="1">
      <line x1="205" y1="18" x2="219" y2="18"/><line x1="231" y1="56" x2="245" y2="56"/>
      <line x1="205" y1="94" x2="219" y2="94"/><line x1="231" y1="132" x2="245" y2="132"/>
      <line x1="205" y1="170" x2="219" y2="170"/><line x1="231" y1="208" x2="245" y2="208"/>
      <line x1="205" y1="246" x2="219" y2="246"/><line x1="231" y1="284" x2="245" y2="284"/>
      <line x1="205" y1="322" x2="219" y2="322"/><line x1="231" y1="360" x2="245" y2="360"/>
      <line x1="205" y1="398" x2="219" y2="398"/><line x1="231" y1="436" x2="245" y2="436"/>
      <line x1="205" y1="474" x2="219" y2="474"/><line x1="231" y1="512" x2="245" y2="512"/>
    </g>
    <g text-anchor="end">
      <text x="200" y="16">Needs assessment call to understand your goals</text><text x="200" y="24">and define the project requirements.</text>
      <text x="200" y="92">Formal quote issued with scope, pricing</text><text x="200" y="100">and an estimated delivery timeline.</text>
      <text x="200" y="168">Kickoff meeting sets roles, milestones</text><text x="200" y="176">and the shared communication plan.</text>
      <text x="200" y="244">Build phase begins with regular progress</text><text x="200" y="252">updates sent at each milestone.</text>
      <text x="200" y="320">Design files and records deposited</text><text x="200" y="328">into IP escrow and verified.</text>
      <text x="200" y="396">Final delivery of the finished product</text><text x="200" y="404">with full documentation package.</text>
      <text x="200" y="472">Go-live support as your team begins</text><text x="200" y="480">using the product in daily work.</text>
    </g>
    <g>
      <text x="250" y="54">Scope confirmed and signed off by both</text><text x="250" y="62">teams before any work starts.</text>
      <text x="250" y="130">Purchase order received and project</text><text x="250" y="138">entered into our scheduling system.</text>
      <text x="250" y="206">Design review with your team to approve</text><text x="250" y="214">drawings, features and materials.</text>
      <text x="250" y="282">Quality checks and testing against every</text><text x="250" y="290">agreed specification and standard.</text>
      <text x="250" y="358">Validation session where you review</text><text x="250" y="366">results and approve the release.</text>
      <text x="250" y="434">Hands-on training for staff so everyone</text><text x="250" y="442">is ready from the first day.</text>
      <text x="250" y="510">Ongoing review meetings to track results</text><text x="250" y="518">and plan future improvements.</text>
    </g>
  </svg>
  <div class="running-foot"><span>www.harbormedical.example</span><span>555-010-4400</span></div>
</section>

<section class="page page--blue back">
  <h2 class="back__title">The Harbor Promise</h2>
  <p class="back__kicker">A Message From Our CEO</p>
  <p class="body-copy">If you are considering a custom device, you likely have many questions about cost, timing and what working with us will look like. We built our guided process to answer those questions before they become worries. Our promise is simple: we will be honest about what is possible, clear about every step and responsive whenever you need us. We measure success by the trust our customers place in us and by the long relationships that follow. Thank you for considering Harbor Medical. We look forward to helping you bring your next product to life.</p>
  <div class="back__sign">Dana Reyes</div>
  <div class="back__role">Chief Executive Officer</div>
  <div class="back__button">Contact Us</div>
  <div class="back__contact">
    info@harbormedical.example<br>
    200 Harbor Way<br>
    Portside, ST 00000<br>
    555-010-4400<br>
    www.harbormedical.example
  </div>
  <div class="back__icon"></div>
</section>

</body>
</html>
```